Startup photo studio needs full suite design (logo, business cards, etc) starting with a website.

We need a website designed for a startup photo studio in the Sacramento area called Silver Lantern Photo Studio. We do portrait work, specializing in the male form and are looking to get into editorial. We would also like to be able to sell prints, posters and canvasses of our work. I would like an elegant but fun design. One of the most important things a portrait photographer needs is the trust of the model. The website would convey honesty, friendliness and warmth as well. I have a domain name with NetHarbor, silverlanternstudio.example email address should be my name with that domain.

Target Market(s)

Art enthusiasts, business portraits, online dating photos

Industry/Entity Type

Professional Photography

Contact Information for Business Card

Simple please. Just logo and contact info. Phone, email, website. no address required

Logo Text

Silver Lantern Photo Studio --- light tells the story

Number of Pages Required

3 page

Font styles to use
Sans Serif

Colors

Designer to choose colors to be used in the design.

Requirements
Must have
• Simple clean design.
Nice to have
• Somehow one of my photos in the design? maybe not...
Should not have
• No weddings!

```html
<!DOCTYPE html>
<html lang="en">
<head>
<meta charset="utf-8">
<title>Silver Lantern Photo Studio</title>
<link rel="stylesheet" href="https://fonts.googleapis.com/css2?family=Dosis:wght@300;400&family=Arimo:wght@400;700&display=swap">
<style>
:root{
  --cyan:#1fb4e8;
  --cyan-soft:#22c4f2;
  --ink:#222;
  --body:#3a3a3a;
  --paper:#f2f2f2;
  --paper-edge:#e2e2e2;
  --dark:#2b2b2b;
  --dark-2:#333;
  --darkest:#1c1c1c;
  --muted:#9a9a9a;
  --light-text:#d8d8d8;
  --line:#555;
}
*{box-sizing:border-box;margin:0;padding:0}
html,body{width:1200px;height:2912px;overflow:hidden;background:var(--darkest)}
body{font-family:Arimo,Arial,sans-serif;color:var(--body);font-size:15px;line-height:20px}
.page{position:relative;width:1200px}
.page--news{height:1640px}
.page--contact{height:1272px}

/* header */
.site-header{position:relative;height:193px;background:radial-gradient(ellipse at 30% 40%,#3a3a3a 0%,#202020 70%);border-bottom:1px solid #111}
.brand{position:absolute;left:62px;top:6px;font-family:Dosis,sans-serif;font-weight:300;font-size:64px;line-height:90px;color:var(--cyan-soft);letter-spacing:0.5px;white-space:nowrap}
.tagline{position:absolute;left:65px;top:122px;font-family:Dosis,sans-serif;font-weight:300;font-size:26px;color:#bdbdbd}
.search{position:absolute;left:890px;top:47px;width:237px;height:30px;display:flex}
.search__field{flex:1;background:#fff;border:1px solid #ccc;font-size:15px;color:#999;padding:5px 8px;line-height:18px}
.search__btn{width:30px;background:#fff;border:1px solid #ccc;border-left:0;display:flex;align-items:center;justify-content:center}
.nav{position:absolute;top:126px;left:490px;display:flex;gap:0;list-style:none}
.nav li{display:flex;align-items:center;font-family:Arimo,Arial,sans-serif;font-size:19px;color:#e6e6e6;margin-right:32px}
.nav li::before{content:"";width:12px;height:12px;border-radius:50%;background:var(--cyan);margin-right:10px}
.nav li.is-active{color:var(--cyan-soft)}

/* light content */
.feature{position:relative;height:612px;background:linear-gradient(180deg,#e9e9e9,var(--paper) 30%,#eaeaea);padding:0 59px}
.feature__title{position:absolute;left:59px;top:232px;top:42px;font-family:Dosis,sans-serif;font-weight:300;font-size:44px;line-height:60px;color:var(--ink);white-space:nowrap}
.feature__title .date{color:var(--cyan-soft)}
.feature__photo{position:absolute;left:59px;top:127px;width:261px;height:308px;border:6px solid #fff;box-shadow:0 0 0 1px #cfcfcf;background:linear-gradient(160deg,#c9ccd0 0%,#8a7a6c 45%,#4d4a4f 100%)}
.feature__text{position:absolute;left:360px;top:124px;width:780px}
.feature__text p{margin-bottom:20px}
.feature__text .lead{font-weight:700;color:#111}
.feature__full{position:absolute;left:59px;top:452px;width:1080px}
a.inline{color:var(--cyan);text-decoration:underline}

/* dark news */
.archive{position:relative;height:688px;background:linear-gradient(180deg,#3a3a3a,var(--dark));padding:64px 59px 0}
.section-title{font-family:Dosis,sans-serif;font-weight:300;font-size:44px;line-height:56px;color:#f0f0f0}
.news-list{list-style:none;margin-top:22px}
.news-item{padding-bottom:14px;margin-bottom:14px;border-bottom:1px dotted var(--line);color:var(--light-text)}
.news-item:last-child{border-bottom:0}
.news-item__head{font-weight:700;color:#fff;margin-bottom:4px}
.news-item__head .date{color:var(--cyan-soft)}
.news-item a{color:var(--cyan);text-decoration:none}

/* footer */
.site-footer{position:relative;height:147px;background:var(--darkest);border-top:1px solid #111}
.credits{position:absolute;left:200px;top:48px;width:400px;text-align:center;font-size:13px;line-height:20px;color:#8a8a8a}
.credits a{color:var(--cyan);text-decoration:underline}
.social{position:absolute;left:863px;top:54px;display:flex;gap:16px;list-style:none}
.social li{width:30px;height:30px}

/* contact form */
.contact{position:relative;height:626px;background:linear-gradient(180deg,#e9e9e9,var(--paper) 30%,#ebebeb);padding:40px 65px 0}
.contact .section-title{color:var(--ink)}
.form{position:absolute;left:65px;top:124px;width:1068px}
.form__row{display:flex;align-items:flex-start;margin-bottom:8px}
.form__label{width:133px;font-weight:700;font-size:15px;color:#111;line-height:26px}
.form__field{flex:1;height:28px;background:#fff;border:1px solid #cfcfcf}
.form__field--area{height:305px}
.form__actions{position:absolute;left:133px;top:410px;display:flex;gap:12px}
.btn{width:77px;height:30px;background:var(--cyan-soft);color:#fff;font-size:15px;line-height:30px;text-align:center}

/* misc */
.misc{position:relative;height:311px;background:linear-gradient(180deg,#3a3a3a,var(--dark));}
.misc__about{position:absolute;left:65px;top:52px;width:720px;color:var(--light-text)}
.misc__about p{margin-top:20px}
.misc__divider{position:absolute;left:805px;top:40px;width:1px;height:240px;background:#444}
.misc__contacts{position:absolute;left:842px;top:52px;width:320px}
.contact-table{margin-top:16px;border-collapse:collapse;font-size:15px;color:var(--light-text)}
.contact-table th{text-align:left;font-weight:700;color:#fff;padding:0 28px 0 0;line-height:22px}
.contact-table td{line-height:22px}
.contact-table a{color:var(--cyan);text-decoration:underline}
</style>
</head>
<body>

<section class="page page--news">
  <header class="site-header">
    <div class="brand">Silver Lantern Photo Studio</div>
    <div class="tagline">Photographer's Portfolio</div>
    <div class="search">
      <div class="search__field">Site Search</div>
      <div class="search__btn"><svg width="18" height="18" viewBox="0 0 18 18"><circle cx="7" cy="7" r="5" fill="none" stroke="#222" stroke-width="2.4"/><line x1="11" y1="11" x2="16" y2="16" stroke="#222" stroke-width="2.8"/></svg></div>
    </div>
    <ul class="nav">
      <li>Home</li><li>About</li><li>Folio</li><li>Services</li><li class="is-active">News</li><li>Contact</li>
    </ul>
  </header>

  <main>
    <article class="feature">
      <h1 class="feature__title"><span class="date">11.05.2011.</span> Lorem ipsum dolor sit amet consectetur</h1>
      <div class="feature__photo" role="img" aria-label="Studio portrait of a male model"></div>
      <div class="feature__text">
        <p class="lead">At vero eos accusamus iusto dignissimos ducimus qui blanditis praesentium voluptatum deleniti atque corrupti quos dolores et quas</p>
        <p>Molestias excepturi sint occaecati cupiditate non provident, similique sunt in culpa qui officia deserunt mollitia animi, id est laborum et dolorum fuga. Et harum quidem rerum facilis est et expedita distinctio. Nam libero tempore, cum soluta nobis est eligendi <a class="inline">optio cumque nihil</a> impedit quo minus id quod maxime placeat facere possimus, omnis voluptas assumenda est, omnis dolor repellendus.</p>
        <p>Temporibus autem quibusdam et aut officiis debitis aut rerum necessitatibus saepe eveniet ut et voluptates repudiandae sint et molestiae non recusandae. Itaque earum rerum hic tenetur a sapiente delectus, ut aut reiciendis voluptatibus maiores alias consequatur aut perferendis doloribus asperiores repellat. Sed ut perspiciatis unde omnis iste natus error sit voluptatem accusantium doloremque laudantium, totam rem aperiam, eaque ipsa quae.</p>
      </div>
      <p class="feature__full">Linventore veritatis et quasi architecto beatae vitae dicta sunt explicabo. Nemo enim ipsam voluptatem quia voluptas sit aspernatur aut odit aut fugit, sed quia consequuntur magni dolores eos qui ratione <a class="inline">voluptatem sequi nesciunt</a>. Neque porro quisquam est, qui dolorem ipsum quia dolor sit amet, consectetur, adipisci velit, sed quia non numquam eius modi tempora incidunt ut labore et dolore magnam aliquam quaerat voluptatem. Ut enim ad minima veniam, quis nostrum exercitationem ullam corporis suscipit laboriosam.</p>
    </article>

    <section class="archive">
      <h2 class="section-title">News Archive</h2>
      <ul class="news-list">
        <li class="news-item">
          <div class="news-item__head"><span class="date">09.05.2011.</span> Sed ut perspiciatis unde omnis iste natus error sit voluptatem accusantium doloremque laudantium</div>
          <p>Nemo enim ipsam voluptatem quia voluptas sit aspernatur aut odit aut fugit, sed quia consequuntur magni dolores eos qui ratione voluptatem sequi nesciunt. Neque porro quisquam est, qui dolorem ipsum quia dolor sit amet, consectetur, adipisci velit, sed quia non numquam eius modi tempora incidunt ut labore et dolore magnam aliquam quaerat voluptatem <a>[...]</a></p>
        </li>
        <li class="news-item">
          <div class="news-item__head"><span class="date">04.05.2011.</span> Sed ut perspiciatis unde omnis iste natus error sit voluptatem accusantium doloremque laudantium</div>
          <p>At vero eos et accusamus et iusto odio dignissimos ducimus qui blanditiis praesentium voluptatum deleniti atque corrupti quos dolores et quas molestias excepturi sint occaecati cupiditate non provident, similique sunt in culpa qui officia deserunt mollitia animi, id est laborum et dolorum fuga. Et harum quidem rerum facilis est et expedita distinctio <a>[...]</a></p>
        </li>
        <li class="news-item">
          <div class="news-item__head"><span class="date">02.05.2011.</span> Sed ut perspiciatis unde omnis iste natus error sit voluptatem accusantium doloremque laudantium</div>
          <p>Nam libero tempore, cum soluta nobis est eligendi optio cumque nihil impedit quo minus id quod maxime placeat facere possimus, omnis voluptas assumenda est, omnis dolor repellendus. Temporibus autem quibusdam et aut officiis debitis aut rerum necessitatibus saepe eveniet ut et voluptates repudiandae sint et molestiae non recusandae <a>[...]</a></p>
        </li>
        <li class="news-item">
          <div class="news-item__head"><span class="date">21.04.2011.</span> Sed ut perspiciatis unde omnis iste natus error sit voluptatem accusantium doloremque laudantium</div>
          <p>Nemo enim ipsam voluptatem quia voluptas sit aspernatur aut odit aut fugit, sed quia consequuntur magni dolores eos qui ratione voluptatem sequi nesciunt. Neque porro quisquam est, qui dolorem ipsum quia dolor sit amet, consectetur, adipisci velit, sed quia non numquam eius modi tempora incidunt ut labore et dolore magnam aliquam quaerat voluptatem <a>[...]</a></p>
        </li>
      </ul>
    </section>
  </main>

  <footer class="site-footer">
    <p class="credits"><a>Website template</a> designed by LayoutForge.example<br><a>3D Models</a> provided by ModelYard.example</p>
    <ul class="social" aria-label="Social links">
      <li><svg width="30" height="30"><rect width="30" height="30" fill="#f26a1b"/></svg></li>
      <li><svg width="30" height="30"><rect width="30" height="30" fill="#2d6fb7"/></svg></li>
      <li><svg width="30" height="30"><rect width="30" height="30" fill="#3fa33f"/></svg></li>
      <li><svg width="30" height="30"><rect width="30" height="30" fill="#3b8fd6"/></svg></li>
      <li><svg width="30" height="30"><rect width="30" height="30" fill="#1b6fa8"/></svg></li>
      <li><svg width="30" height="30"><rect width="30" height="30" fill="#e0401c"/></svg></li>
    </ul>
  </footer>
</section>

<section class="page page--contact">
  <header class="site-header">
    <div class="brand">Silver Lantern Photo Studio</div>
    <div class="tagline">Photographer's Portfolio</div>
    <div class="search">
      <div class="search__field">Site Search</div>
      <div class="search__btn"><svg width="18" height="18" viewBox="0 0 18 18"><circle cx="7" cy="7" r="5" fill="none" stroke="#222" stroke-width="2.4"/><line x1="11" y1="11" x2="16" y2="16" stroke="#222" stroke-width="2.8"/></svg></div>
    </div>
    <ul class="nav">
      <li>Home</li><li>About</li><li>Folio</li><li>Services</li><li>News</li><li class="is-active">Contact</li>
    </ul>
  </header>

  <main>
    <section class="contact">
      <h2 class="section-title">Contact Form</h2>
      <div class="form">
        <div class="form__row"><span class="form__label">Your Name:</span><span class="form__field"></span></div>
        <div class="form__row"><span class="form__label">Your E-mail:</span><span class="form__field"></span></div>
        <div class="form__row"><span class="form__label">Your Message:</span><span class="form__field form__field--area"></span></div>
        <div class="form__actions"><span class="btn">Clear</span><span class="btn">Send</span></div>
      </div>
    </section>

    <section class="misc">
      <div class="misc__about">
        <h2 class="section-title">Miscellaneous</h2>
        <p>Sed ut perspiciatis unde omnis iste natus error sit voluptatem accusantium doloremque laudantium, totam rem aperiam, eaque ipsa quae ab illo inventore veritatis et quasi architecto beatae vitae dicta sunt explicabo. Nemo enim ipsam voluptatem quia voluptas sit aspernatur aut odit aut fugit, sed quia consequuntur magni dolores eos qui ratione voluptatem sequi nesciunt. Neque porro quisquam est.</p>
      </div>
      <div class="misc__divider"></div>
      <div class="misc__contacts">
        <h2 class="section-title">My Contacts</h2>
        <table class="contact-table">
          <tr><th>Country:</th><td>USA</td></tr>
          <tr><th>State:</th><td>California</td></tr>
          <tr><th>City:</th><td>Sacramento</td></tr>
          <tr><th>Telephone:</th><td>+1 916 555 0142</td></tr>
          <tr><th>Email:</th><td><a>hello@silverlanternstudio.example</a></td></tr>
        </table>
      </div>
    </section>
  </main>

  <footer class="site-footer">
    <p class="credits"><a>Website template</a> designed by LayoutForge.example<br><a>3D Models</a> provided by ModelYard.example</p>
    <ul class="social" aria-label="Social links">
      <li><svg width="30" height="30"><rect width="30" height="30" fill="#f26a1b"/></svg></li>
      <li><svg width="30" height="30"><rect width="30" height="30" fill="#2d6fb7"/></svg></li>
      <li><svg width="30" height="30"><rect width="30" height="30" fill="#3fa33f"/></svg></li>
      <li><svg width="30" height="30"><rect width="30" height="30" fill="#3b8fd6"/></svg></li>
      <li><svg width="30" height="30"><rect width="30" height="30" fill="#1b6fa8"/></svg></li>
      <li><svg width="30" height="30"><rect width="30" height="30" fill="#e0401c"/></svg></li>
    </ul>
  </footer>
</section>

</body>
</html>
```